Website for Apartment Rental in Prague

I would like to create designs of my website focused on luxury apartment rentals in Prague, Czech Republic. I created initial mock-ups, They are all attached. I need to design homepage and subpage. The mock-ups were created by combining elements from different websites that I liked but I need you to create a design that is unique and original. The attached files a only a guidance for the structure of the website but not for the design. Try to be creative.

Industry/Entity Type

Apartment

```html
<!DOCTYPE html>
<html lang="en">
<head>
<meta charset="utf-8">
<title>Vltava Stay — Luxury Apartments in Prague</title>
<link href="https://fonts.googleapis.com/css2?family=Cormorant+Garamond:wght@400;500;600&family=Manrope:wght@400;500;600;700&display=swap" rel="stylesheet">
<style>
:root{
  --navy:#1e2a36;
  --navy-soft:#2a3846;
  --brass:#b8925a;
  --brass-dark:#9c7a47;
  --cream:#f6f1ea;
  --sand:#ebe3d7;
  --ink:#1e2a36;
  --text:#5b6069;
  --muted:#8f949b;
  --line:#e4dccf;
  --white:#ffffff;
}
*{box-sizing:border-box;margin:0;padding:0}
html,body{width:1200px;height:4091px;overflow:hidden}
body{background:var(--white);font-family:'Manrope',Arial,sans-serif;color:var(--text);font-size:14px}
svg{display:block}
.abs{position:absolute}
section,header,footer{position:relative;width:1200px}
.serif{font-family:'Cormorant Garamond',Georgia,serif}
.eyebrow-rule{width:56px;height:2px;background:var(--brass)}

/* top bar */
.topbar{height:40px;background:var(--navy);color:#c7ccd2;font-size:12px;display:flex;align-items:center;justify-content:space-between;padding:0 80px}
.topbar .group{display:flex;align-items:center;gap:28px}
.topbar .item{display:flex;align-items:center;gap:8px}
.flag{width:16px;height:10px;background:#c7ccd2;display:block}
.social-dots{display:flex;gap:10px}
.social-dots i{width:9px;height:9px;border-radius:50%;background:#c7ccd2;display:block}

/* header */
.site-header{height:90px;border-bottom:1px solid var(--line);display:flex;align-items:center;justify-content:space-between;padding:0 80px}
.logo{display:flex;align-items:center;gap:12px;font-size:20px;font-weight:700;letter-spacing:3px;color:var(--ink)}
.logo-mark{width:14px;height:14px;background:var(--brass);display:block}
.nav{display:flex;gap:30px;font-size:13.5px;font-weight:500;color:var(--ink)}
.nav .active{color:var(--brass-dark)}

/* hero */
.hero{height:640px;background:var(--cream)}
.hero-photo{left:440px;top:40px;width:680px;height:560px;background:linear-gradient(135deg,#6b4a32 0%,#a9a39a 42%,#e4e1dc 72%,#f4f3f1 100%)}
.hero-copy{left:80px;top:196px;width:420px}
.hero-copy .kicker{font-size:14px;font-weight:600;letter-spacing:6px;color:var(--brass-dark);margin-top:22px}
.hero-copy .city{font-size:118px;font-weight:500;line-height:1;color:var(--ink);margin-top:10px;letter-spacing:1px}
.hero-pager{left:80px;top:548px;display:flex;gap:10px}
.hero-pager i{width:28px;height:3px;background:#cdc3b4;display:block}
.hero-pager i.on{width:56px;background:var(--brass)}

/* booking */
.booking{height:260px}
.section-title{width:1200px;text-align:center;font-size:38px;font-weight:500;color:var(--ink);letter-spacing:.5px}
.booking .section-title{position:absolute;top:52px;left:0}
.booking-form{left:80px;top:132px;width:1040px;height:96px;border:1px solid var(--line);background:var(--white);display:grid;grid-template-columns:140px 140px 80px 80px 80px 1fr 120px 170px;column-gap:10px;align-items:end;padding:0 24px 18px}
.field label{display:block;font-size:11px;font-weight:600;color:var(--ink);margin-bottom:7px;white-space:nowrap}
.field .box{height:40px;background:var(--cream);border:1px solid var(--line);font-size:11.5px;color:var(--muted);display:flex;align-items:center;justify-content:space-between;padding:0 10px}
.check-btn{height:40px;background:var(--navy);color:var(--white);font-size:11.5px;font-weight:700;letter-spacing:1.2px;display:flex;align-items:center;justify-content:center}

/* story blocks */
.block-title{font-size:46px;font-weight:500;color:var(--ink);line-height:1.05;margin-top:20px}
.body-copy{font-size:14px;line-height:26px;margin-top:22px}
.about{height:600px}
.about-frame{left:112px;top:92px;width:540px;height:440px;border:1px solid var(--brass)}
.about-photo{left:80px;top:60px;width:540px;height:440px;background:linear-gradient(160deg,#e9e4da 0%,#b89d78 45%,#5a3e28 100%)}
.about-copy{left:720px;top:150px;width:400px}
.outline-btn{margin-top:30px;width:150px;height:44px;border:1.5px solid var(--ink);color:var(--ink);font-size:11.5px;font-weight:700;letter-spacing:1.5px;display:flex;align-items:center;justify-content:center}

.interior{height:600px;background:var(--navy)}
.interior-copy{left:80px;top:170px;width:430px;color:#d6dbe0}
.interior-copy .block-title{color:var(--white)}
.interior-copy .body-copy{color:#c3c9d0}
.byline{margin-top:26px;font-size:12px;font-weight:700;letter-spacing:2px;color:var(--brass)}
.interior-photo{left:600px;top:60px;width:520px;height:480px;background:linear-gradient(170deg,#d8c29d 0%,#efe7da 45%,#b48246 100%)}

/* rentals */
.rentals{height:1000px;background:var(--white)}
.rentals .section-title{position:absolute;top:64px;left:0}
.cards{left:80px;top:150px;width:1040px;display:grid;grid-template-columns:repeat(3,332px);column-gap:22px;row-gap:34px}
.card{height:380px;border:1px solid var(--line);background:var(--white);position:relative}
.card .photo{height:230px;position:relative}
.price-tag{position:absolute;left:0;bottom:0;background:var(--brass);color:var(--white);font-family:'Cormorant Garamond',Georgia,serif;font-size:24px;font-weight:600;padding:6px 18px}
.card .info{padding:20px 24px 0;height:94px}
.card h3{font-family:'Cormorant Garamond',Georgia,serif;font-size:25px;font-weight:600;color:var(--ink);line-height:1.1}
.card .loc{margin-top:8px;font-size:12.5px;display:flex;gap:7px;align-items:center}
.card .meta{height:54px;border-top:1px solid var(--line);display:flex;align-items:center;justify-content:space-between;padding:0 24px}
.feats{display:flex;gap:16px;font-size:11.5px;color:var(--muted)}
.feats span{display:flex;gap:5px;align-items:center}
.acts{display:flex;gap:12px}
.overlay{position:absolute;left:0;top:0;width:330px;height:230px;background:rgba(30,42,54,.82);display:flex;justify-content:center;align-items:center;gap:10px}
.overlay span{font-size:11.5px;font-weight:700;letter-spacing:1px;width:112px;height:42px;display:flex;align-items:center;justify-content:center}
.overlay .ghost{border:1.5px solid var(--white);color:var(--white)}
.overlay .solid{background:var(--brass);color:var(--white)}

/* testimonials */
.testimonials{height:420px;background:var(--sand)}
.thumb{top:170px;width:150px;height:80px;background:linear-gradient(90deg,#6c7a80,#c7b7a6,#4d5458)}
.stars{left:0;top:72px;width:1200px;display:flex;justify-content:center}
.quote{left:290px;top:110px;width:620px;text-align:center;font-family:'Cormorant Garamond',Georgia,serif;font-size:23px;line-height:34px;color:var(--ink)}
.arrow-btn{top:166px;width:44px;height:44px;border-radius:50%;border:1px solid var(--brass);display:flex;align-items:center;justify-content:center}
.avatar{left:572px;top:262px;width:56px;height:56px;border-radius:50%;background:#c9a58a;border:3px solid var(--white)}
.author{left:0;top:332px;width:1200px;text-align:center;font-size:12px;font-weight:700;letter-spacing:2px;color:var(--brass-dark)}
.chat{left:900px;top:378px;width:220px;height:42px;background:var(--navy);color:var(--white);font-size:12px;font-weight:700;letter-spacing:1px;display:flex;align-items:center;gap:14px;padding:0 18px}
.chat .label{flex:1}

/* footer */
.site-footer{height:441px;background:var(--navy);color:#b9c0c8}
.f-links{top:70px;font-size:13px;line-height:24px}
.f-head{font-size:12px;font-weight:700;letter-spacing:2px;color:var(--white)}
.f-social{left:860px;top:102px;display:flex;gap:14px}
.f-social i{width:14px;height:14px;border-radius:50%;background:#8d97a2;display:block}
.news-label{left:120px;top:194px}
.news-input{left:120px;top:226px;width:560px;height:44px;border-bottom:1px solid #56636f;display:flex;justify-content:space-between;align-items:center;font-size:12.5px}
.news-input .go{color:var(--brass);font-weight:700;letter-spacing:1.5px;font-size:12px}
.f-contact{left:860px;top:194px}
.f-contact .lines{margin-top:14px;font-size:13px;line-height:24px}
.f-divider{left:80px;top:350px;width:1040px;height:1px;background:#3a4856}
.copyright{left:0;top:384px;width:1200px;text-align:center;font-size:11px;letter-spacing:1.5px;color:#9aa3ad}
.to-top{left:1082px;top:370px;width:40px;height:40px;border-radius:50%;background:var(--brass);display:flex;align-items:center;justify-content:center}
</style>
</head>
<body>

<svg width="0" height="0" style="position:absolute">
  <symbol id="i-bed" viewBox="0 0 14 10"><path d="M1 1v8M1 6h12v3M3 4h4v2" fill="none" stroke="currentColor" stroke-width="1.2"/></symbol>
  <symbol id="i-bath" viewBox="0 0 14 10"><path d="M1 5h12v1a3 3 0 0 1-3 3H4a3 3 0 0 1-3-3zM3 5V2a1 1 0 0 1 2 0" fill="none" stroke="currentColor" stroke-width="1.2"/></symbol>
  <symbol id="i-guest" viewBox="0 0 10 10"><circle cx="5" cy="3" r="2" fill="none" stroke="currentColor" stroke-width="1.2"/><path d="M1 10a4 4 0 0 1 8 0" fill="none" stroke="currentColor" stroke-width="1.2"/></symbol>
  <symbol id="i-pin" viewBox="0 0 9 12"><path d="M4.5 0A4.5 4.5 0 0 0 0 4.5C0 8 4.5 12 4.5 12S9 8 9 4.5A4.5 4.5 0 0 0 4.5 0zm0 6.3a1.8 1.8 0 1 1 0-3.6 1.8 1.8 0 0 1 0 3.6z" fill="currentColor"/></symbol>
  <symbol id="i-share" viewBox="0 0 12 12"><circle cx="2.5" cy="6" r="2" fill="currentColor"/><circle cx="9.5" cy="2.5" r="2" fill="currentColor"/><circle cx="9.5" cy="9.5" r="2" fill="currentColor"/><path d="M2.5 6l7-3.5M2.5 6l7 3.5" stroke="currentColor"/></symbol>
  <symbol id="i-star" viewBox="0 0 12 12"><path d="M6 .8l1.5 3.4 3.7.3-2.8 2.4.9 3.6L6 8.6 2.7 10.5l.9-3.6L.8 4.5l3.7-.3z" fill="none" stroke="currentColor"/></symbol>
  <symbol id="i-cal" viewBox="0 0 11 11"><rect x=".5" y="1.5" width="10" height="9" fill="none" stroke="currentColor"/><path d="M.5 4h10" stroke="currentColor"/></symbol>
  <symbol id="i-caret" viewBox="0 0 8 5"><path d="M0 0h8L4 5z" fill="currentColor"/></symbol>
  <symbol id="i-fullstar" viewBox="0 0 13 13"><path d="M6.5 0l1.9 4.1 4.4.4-3.3 3 1 4.5-4-2.4-4 2.4 1-4.5-3.3-3 4.4-.4z" fill="currentColor"/></symbol>
</svg>

<header>
  <div class="topbar">
    <div class="group">
      <span class="item"><svg width="12" height="9" viewBox="0 0 12 9"><rect x=".5" y=".5" width="11" height="8" fill="none" stroke="#c7ccd2"/><path d="M.5 .5 6 5l5.5-4.5" fill="none" stroke="#c7ccd2"/></svg>hello@vltavastay.cz</span>
      <span class="item"><svg width="10" height="10" viewBox="0 0 10 10"><path d="M2 1l2 2-1 1.5c.8 1.4 1.6 2.2 3 3L7.5 6l2 2-1.5 1.5C4.5 9 1 5.5.5 2z" fill="#c7ccd2"/></svg>+420 | 555 | 0148</span>
      <span class="item"><i class="flag"></i>EN</span>
    </div>
    <div class="group">
      <span>Login</span><span>|</span><span>Register</span>
      <div class="social-dots"><i></i><i></i><i></i><i></i><i></i><i></i></div>
    </div>
  </div>
  <div class="site-header">
    <div class="logo"><i class="logo-mark"></i>VLTAVA STAY</div>
    <nav class="nav">
      <span class="active">Apartments</span><span>Location</span><span>Services</span><span>Gallery</span><span>News</span><span>Exclusive Offers &amp; Tours</span><span>For Families</span><span>Contact Us</span>
    </nav>
  </div>
</header>

<section class="hero">
  <div class="abs hero-copy">
    <div class="eyebrow-rule"></div>
    <div class="kicker">BEING HOME IN</div>
    <div class="city serif">Prague</div>
  </div>
  <div class="abs hero-pager"><i></i><i class="on"></i><i></i></div>
  <div class="abs hero-photo" role="img" aria-label="Bright living room with brown sectional sofa, wall-mounted TV on wood panelling and patterned rug"></div>
</section>

<section class="booking">
  <h2 class="section-title serif">Official Site Best Price Guaranteed</h2>
  <form class="abs booking-form">
    <div class="field"><label>Check in Date :</label><div class="box">11-17-2017<svg width="11" height="11" style="color:#8f949b"><use href="#i-cal"/></svg></div></div>
    <div class="field"><label>Check Out Date :</label><div class="box">11-19-2017<svg width="11" height="11" style="color:#8f949b"><use href="#i-cal"/></svg></div></div>
    <div class="field"><label>Adults :</label><div class="box">2<svg width="8" height="5" style="color:#8f949b"><use href="#i-caret"/></svg></div></div>
    <div class="field"><label>Children :</label><div class="box">0<svg width="8" height="5" style="color:#8f949b"><use href="#i-caret"/></svg></div></div>
    <div class="field"><label>Infants :</label><div class="box">0<svg width="8" height="5" style="color:#8f949b"><use href="#i-caret"/></svg></div></div>
    <div class="field"><label>Promotional Code :</label><div class="box"></div></div>
    <div class="field"><label>Rental Unit :</label><div class="box">Rental Unit<svg width="8" height="5" style="color:#8f949b"><use href="#i-caret"/></svg></div></div>
    <div class="check-btn">CHECK AVAILABILITY</div>
  </form>
</section>

<section class="about">
  <div class="abs about-frame"></div>
  <div class="abs about-photo" role="img" aria-label="Open-plan apartment with dining bar, pendant lights and lounge by the window"></div>
  <div class="abs about-copy">
    <div class="eyebrow-rule"></div>
    <h2 class="block-title serif">About Us</h2>
    <p class="body-copy">Lorem ipsum dolor sit amet, consectetuer adipiscing elit. Aenean commodo ligula eget dolor aenean massa. Cum sociis natoque penatibus et magnis dis parturient montes, nascetur ridiculus mus. Donec quam felis, ultricies nec pellentesque.</p>
    <div class="outline-btn">READ MORE</div>
  </div>
</section>

<section class="interior">
  <div class="abs interior-copy">
    <div class="eyebrow-rule"></div>
    <h2 class="block-title serif">Interior Design</h2>
    <p class="body-copy">Lorem ipsum dolor sit amet, consectetuer adipiscing elit. Aenean commodo ligula eget dolor aenean massa. Cum sociis natoque penatibus et magnis dis parturient montes, nascetur ridiculus mus. Donec quam felis, ultricies nec pellentesque.</p>
    <div class="byline">BY : PETR HOLAN</div>
  </div>
  <div class="abs interior-photo" role="img" aria-label="Warm bedroom and hallway with wooden floor and pendant lamp"></div>
</section>

<section class="rentals">
  <h2 class="section-title serif">Luxury Apartment Rentals</h2>
  <div class="abs cards">
    <article class="card">
      <div class="photo" role="img" aria-label="Bedroom with white bedding and balcony doors" style="background:linear-gradient(135deg,#d9d4cc,#8b8278)"><span class="price-tag">$200</span></div>
      <div class="info"><h3>Family Apartment</h3><div class="loc"><svg width="9" height="12" style="color:#b8925a"><use href="#i-pin"/></svg>Prague</div></div>
      <div class="meta"><div class="feats"><span><svg width="14" height="10"><use href="#i-bed"/></svg>3 Bedrooms</span><span><svg width="14" height="10"><use href="#i-bath"/></svg>2 Bathroom</span><span><svg width="10" height="10"><use href="#i-guest"/></svg>6 Adult</span></div><div class="acts" style="color:#1e2a36"><svg width="12" height="12"><use href="#i-share"/></svg><svg width="12" height="12"><use href="#i-star"/></svg></div></div>
    </article>
    <article class="card">
      <div class="photo" role="img" aria-label="Bright apartment living area" style="background:linear-gradient(135deg,#f1dcc4,#c98e5c)"><span class="price-tag">$200</span></div>
      <div class="overlay"><span class="ghost">DETAILS</span><span class="solid">BOOK NOW</span></div>
      <div class="info"><h3>Family Apartment</h3><div class="loc"><svg width="9" height="12" style="color:#b8925a"><use href="#i-pin"/></svg>Prague</div></div>
      <div class="meta"><div class="feats"><span><svg width="14" height="10"><use href="#i-bed"/></svg>3 Bedrooms</span><span><svg width="14" height="10"><use href="#i-bath"/></svg>2 Bathroom</span><span><svg width="10" height="10"><use href="#i-guest"/></svg>6 Adult</span></div><div class="acts" style="color:#1e2a36"><svg width="12" height="12"><use href="#i-share"/></svg><svg width="12" height="12"><use href="#i-star"/></svg></div></div>
    </article>
    <article class="card">
      <div class="photo" role="img" aria-label="White living room with sofa and shuttered windows" style="background:linear-gradient(135deg,#c8ccd0,#f1f2f3)"><span class="price-tag">$200</span></div>
      <div class="info"><h3>Family Apartment</h3><div class="loc"><svg width="9" height="12" style="color:#b8925a"><use href="#i-pin"/></svg>Czech</div></div>
      <div class="meta"><div class="feats"><span><svg width="14" height="10"><use href="#i-bed"/></svg>3 Bedrooms</span><span><svg width="14" height="10"><use href="#i-bath"/></svg>2 Bathroom</span><span><svg width="10" height="10"><use href="#i-guest"/></svg>6 Adult</span></div><div class="acts" style="color:#1e2a36"><svg width="12" height="12"><use href="#i-share"/></svg><svg width="12" height="12"><use href="#i-star"/></svg></div></div>
    </article>
    <article class="card">
      <div class="photo" role="img" aria-label="Dining room with long white table and pendant lamp" style="background:linear-gradient(135deg,#8a6a4a,#e9dccb)"><span class="price-tag">$200</span></div>
      <div class="info"><h3>Family Apartment</h3><div class="loc"><svg width="9" height="12" style="color:#b8925a"><use href="#i-pin"/></svg>Prague</div></div>
      <div class="meta"><div class="feats"><span><svg width="14" height="10"><use href="#i-bed"/></svg>3 Bedrooms</span><span><svg width="14" height="10"><use href="#i-bath"/></svg>2 Bathroom</span><span><svg width="10" height="10"><use href="#i-guest"/></svg>6 Adult</span></div><div class="acts" style="color:#1e2a36"><svg width="12" height="12"><use href="#i-share"/></svg><svg width="12" height="12"><use href="#i-star"/></svg></div></div>
    </article>
    <article class="card">
      <div class="photo" role="img" aria-label="Grey sofa with colourful cushions by a window" style="background:linear-gradient(135deg,#e7e7e5,#9a9a98)"><span class="price-tag">$200</span></div>
      <div class="info"><h3>Family Apartment</h3><div class="loc"><svg width="9" height="12" style="color:#b8925a"><use href="#i-pin"/></svg>Czech</div></div>
      <div class="meta"><div class="feats"><span><svg width="14" height="10"><use href="#i-bed"/></svg>3 Bedrooms</span><span><svg width="14" height="10"><use href="#i-bath"/></svg>2 Bathroom</span><span><svg width="10" height="10"><use href="#i-guest"/></svg>6 Adult</span></div><div class="acts" style="color:#1e2a36"><svg width="12" height="12"><use href="#i-share"/></svg><svg width="12" height="12"><use href="#i-star"/></svg></div></div>
    </article>
    <article class="card">
      <div class="photo" role="img" aria-label="Lounge with purple sofas and glossy floor" style="background:linear-gradient(135deg,#3c3a44,#d8d6dc)"><span class="price-tag">$200</span></div>
      <div class="info"><h3>Family Apartment</h3><div class="loc"><svg width="9" height="12" style="color:#b8925a"><use href="#i-pin"/></svg>Prague</div></div>
      <div class="meta"><div class="feats"><span><svg width="14" height="10"><use href="#i-bed"/></svg>3 Bedrooms</span><span><svg width="14" height="10"><use href="#i-bath"/></svg>2 Bathroom</span><span><svg width="10" height="10"><use href="#i-guest"/></svg>6 Adult</span></div><div class="acts" style="color:#1e2a36"><svg width="12" height="12"><use href="#i-share"/></svg><svg width="12" height="12"><use href="#i-star"/></svg></div></div>
    </article>
  </div>
</section>

<section class="testimonials">
  <div class="abs thumb" style="left:0" role="img" aria-label="Row of guest portrait thumbnails"></div>
  <div class="abs thumb" style="left:1050px" role="img" aria-label="Row of guest portrait thumbnails"></div>
  <div class="abs stars" style="color:#b8925a;gap:6px"><svg width="13" height="13"><use href="#i-fullstar"/></svg><svg width="13" height="13"><use href="#i-fullstar"/></svg><svg width="13" height="13"><use href="#i-fullstar"/></svg><svg width="13" height="13"><use href="#i-fullstar"/></svg><svg width="13" height="13"><use href="#i-fullstar"/></svg></div>
  <div class="abs arrow-btn" style="left:210px"><svg width="16" height="12" viewBox="0 0 16 12"><path d="M15 6H2M6 1 1 6l5 5" fill="none" stroke="#1e2a36" stroke-width="1.5"/></svg></div>
  <div class="abs arrow-btn" style="left:946px"><svg width="16" height="12" viewBox="0 0 16 12"><path d="M1 6h13M10 1l5 5-5 5" fill="none" stroke="#1e2a36" stroke-width="1.5"/></svg></div>
  <p class="abs quote">Lorem ipsum dolor sit amet, consectetuer adipiscing elit. Aenean commodo ligula eget dolor cum sociis et magnis dis parturient montes, nascetur ridiculus mus donec quam felis</p>
  <div class="abs avatar" role="img" aria-label="Guest portrait"></div>
  <div class="abs author">MARTA KLIMOVA</div>
  <div class="abs chat">
    <svg width="14" height="12" viewBox="0 0 14 12"><path d="M1 1h12v7H5l-3 3V8H1z" fill="none" stroke="#fff" stroke-width="1.3"/></svg>
    <span class="label">LIVE CHAT</span>
    <svg width="10" height="6" viewBox="0 0 10 6"><path d="M1 1l4 4 4-4" fill="none" stroke="#fff" stroke-width="1.5"/></svg>
  </div>
</section>

<footer class="site-footer">
  <div class="abs f-links" style="left:120px">Customer service<br>How it works</div>
  <div class="abs f-links" style="left:340px">About us<br>Testimonials</div>
  <div class="abs f-links" style="left:560px">Press<br>Contacts</div>
  <div class="abs f-head" style="left:860px;top:74px">SOCIAL</div>
  <div class="abs f-social"><i></i><i></i><i></i><i></i><i></i></div>

  <div class="abs f-head news-label">NEWSLETTER</div>
  <div class="abs news-input"><span>Email Adress</span><span class="go">SIGN IN</span></div>

  <div class="abs f-contact">
    <div class="f-head">CONTACTS</div>
    <div class="lines">+420 | 555 | 0192<br>12 Karlova Street, Prague 110 00</div>
  </div>

  <div class="abs f-divider"></div>
  <div class="abs copyright">COPYRIGHT 2017 | ALL RIGHT RESERVED</div>
  <div class="abs to-top"><svg width="12" height="8" viewBox="0 0 12 8"><path d="M1 7l5-5 5 5" fill="none" stroke="#fff" stroke-width="1.8"/></svg></div>
</footer>

</body>
</html>
```